Ridgeline Wild Craft DL flyer

I'm looking for a new flyer for my startup business. In Darwin Australia.
Aimed at family's and short stay tourists the "Ridgeline Wild Craft" 4 hr tour will give people a basic understanding of some essential bush survival skills in the Australian Outback.
things covered in this 4 hr tour are
1. Finding water.
2. finding food.
3. Finding/making shelter and fire.
4. Finding your way home.

The tour will pick clients up in an air conditioned purpose build 4WD and take them to a nearby bushland area where they will have the opportunity to catch and harvest some native bushtucker.
They will then be able to find/harvest some water for survival situations.
While we cook our bush tucker they will also learn to find their way home through ancient navigation techniques as well.

Clients will then be dropped back to their accomodation with some fun and vital knowledge of surviving in the Australian outback.
At the end of the tour the group will be able to take home a basic survival kit which they will be able to use through the skills they just gained on the tour.

I'd like a two sided DL size flyer emphasising the following points.
4hr/half day tour
Fun for the family
Free survival kit included.
Eat what you catch
Learn essential survival skills
Provided buy an experienced and passionate bushman.
$150/head including transfers.

I'll provide some pictures for the flyer and any extra content you require.

Target Market(s)

Family's
Short stay tourists

Industry/Entity Type

Tourism

Colors

Designer to choose colors to be used in the design.

Requirements
Must have
• As per brief
Nice to have
• Any extra content and flair designers would like to add
Should not have
• Any images which aren't Australian

```html
<!DOCTYPE html>
<html lang="en">
<head>
<meta charset="utf-8">
<title>Ridgeline Wild Craft – DL Flyer</title>
<link rel="stylesheet" href="https://fonts.googleapis.com/css2?family=Cinzel:wght@400;700&family=Open+Sans:wght@400;600;700&display=swap">
<style>
  :root{
    --blue:#3fb6e6;
    --blue-deep:#1e8fc4;
    --ink:#111214;
    --paper:#f3f3f3;
    --stage:#e4e4e4;
    --white:#ffffff;
  }
  html,body{margin:0;padding:0;overflow:hidden}
  body{width:1200px;height:1200px;background:var(--stage);position:relative;font-family:"Open Sans",sans-serif}
  .flyer{position:absolute;top:192px;width:408px;height:816px;box-shadow:0 6px 18px rgba(0,0,0,.25)}
  .flyer--front{left:160px}
  .flyer--back{left:660px}
  .flyer svg{display:block;width:100%;height:100%}
  .fill-blue{fill:var(--blue)}
  .fill-ink{fill:var(--ink)}
  .fill-white{fill:var(--white)}
  .stroke-blue{fill:none;stroke:var(--blue);stroke-width:5}
  .title-main{font-family:"Cinzel",serif;font-size:40px;font-weight:700;fill:var(--blue);letter-spacing:1px}
  .title-sub{font-family:"Cinzel",serif;font-size:24px;fill:#e8e8e8;letter-spacing:2px}
  .price{font-family:"Cinzel",serif;font-size:56px;fill:var(--blue)}
  .price-note{font-family:"Cinzel",serif;font-size:13px;fill:var(--blue)}
  .price-tag{font-family:"Cinzel",serif;font-size:17px;font-weight:700;fill:var(--white);letter-spacing:1px}
  .body-copy{font-family:"Open Sans",sans-serif;font-size:14.5px;font-weight:600;fill:#1a1a1a}
  .body-copy--small{font-size:12.8px}
  .pill-text{font-family:"Open Sans",sans-serif;font-size:14px;fill:var(--white)}
  .list-text{font-family:"Open Sans",sans-serif;font-size:13.5px;fill:#1a1a1a}
  .feature-text{font-family:"Open Sans",sans-serif;font-size:13px;font-weight:600;fill:#1a1a1a}
  .call{font-family:"Cinzel",serif;font-size:22px;font-weight:700;letter-spacing:1px}
  .call--dark{fill:var(--ink)}
  .call--light{fill:var(--white)}
  .web{font-family:"Open Sans",sans-serif;font-size:12px;font-weight:600;fill:var(--white);letter-spacing:2.2px}
  .icon-line{fill:none;stroke:var(--ink);stroke-width:2.2;stroke-linecap:round;stroke-linejoin:round}
</style>
</head>
<body>

<!-- FRONT SIDE -->
<div class="flyer flyer--front">
<svg viewBox="0 0 475 952" xmlns="http://www.w3.org/2000/svg">
  <defs>
    <linearGradient id="front-paper" x1="0" y1="0" x2="0" y2="1">
      <stop offset="0" stop-color="#ffffff"/>
      <stop offset=".5" stop-color="#dcdcdc"/>
      <stop offset="1" stop-color="#f6f6f6"/>
    </linearGradient>
    <linearGradient id="front-top" x1="0" y1="0" x2="1" y2="1">
      <stop offset="0" stop-color="#0b0b0c"/>
      <stop offset=".6" stop-color="#2a2b2e"/>
      <stop offset="1" stop-color="#0b0b0c"/>
    </linearGradient>
    <linearGradient id="bush-photo" x1="0" y1="0" x2="0" y2="1">
      <stop offset="0" stop-color="#f4f6f2"/>
      <stop offset=".35" stop-color="#7f9a5a"/>
      <stop offset=".7" stop-color="#5b7a36"/>
      <stop offset="1" stop-color="#9a5a2c"/>
    </linearGradient>
    <linearGradient id="guide-photo" x1="0" y1="0" x2="1" y2="1">
      <stop offset="0" stop-color="#cfc7b6"/>
      <stop offset=".6" stop-color="#9c8b72"/>
      <stop offset="1" stop-color="#e0e0dc"/>
    </linearGradient>
    <linearGradient id="front-blue" x1="0" y1="0" x2="1" y2="0">
      <stop offset="0" stop-color="#1e8fc4"/>
      <stop offset="1" stop-color="#55c7f0"/>
    </linearGradient>
    <filter id="front-shadow" x="-20%" y="-20%" width="140%" height="140%">
      <feDropShadow dx="0" dy="6" stdDeviation="6" flood-opacity=".35"/>
    </filter>
    <clipPath id="front-hero-clip">
      <polygon points="232,125 467,360 232,595 -3,360"/>
    </clipPath>
  </defs>

  <rect class="flyer-paper" width="475" height="952" fill="url(#front-paper)"/>

  <!-- header band -->
  <polygon class="header-band" points="0,0 475,0 475,20 232,240 0,18" fill="url(#front-top)"/>
  <polygon class="accent-stripe fill-blue" points="0,18 232,240 232,252 0,30"/>
  <polygon class="accent-stripe fill-blue" points="475,20 232,240 232,252 475,32"/>
  <polygon class="accent-stripe fill-ink" points="475,105 340,240 355,255 475,135"/>
  <polygon class="accent-stripe fill-ink" points="0,570 70,500 85,515 0,598"/>

  <text class="title-main" x="237" y="58" text-anchor="middle">RIDGELINE</text>
  <text class="title-sub" x="237" y="92" text-anchor="middle">WILD CRAFT</text>

  <!-- hero diamond -->
  <g filter="url(#front-shadow)">
    <polygon class="fill-white" points="232,118 474,360 232,602 -10,360"/>
  </g>
  <g clip-path="url(#front-hero-clip)">
    <rect role="img" aria-label="Photo of outback bushland with termite mounds" x="0" y="125" width="475" height="470" fill="url(#bush-photo)"/>
  </g>
  <polygon class="stroke-blue" points="232,125 467,360 232,595 -3,360"/>

  <!-- price diamond -->
  <g filter="url(#front-shadow)">
    <polygon class="fill-white" points="355,358 473,476 355,594 237,476"/>
  </g>
  <polygon class="stroke-blue" points="355,366 465,476 355,586 245,476"/>
  <text class="price" x="358" y="477" text-anchor="middle">$150</text>
  <text class="price-note" x="358" y="494" text-anchor="middle">HEAD INCLUDING</text>
  <rect class="fill-ink" x="288" y="500" width="139" height="23"/>
  <text class="price-tag" x="357" y="518" text-anchor="middle">TRANSFERS</text>

  <!-- intro -->
  <text class="body-copy">
    <tspan x="31" y="636" textLength="409" lengthAdjust="spacing">4 hr tour will give people a basic understanding of</tspan>
    <tspan x="31" y="655" textLength="409" lengthAdjust="spacing">some essential bush survival skills in the Australian</tspan>
    <tspan x="31" y="674">Outback.</tspan>
  </text>

  <!-- guide photo area (kept clear of the topic list) -->
  <path role="img" aria-label="Photo of the bushman guide in a wide-brim hat" d="M372,700 L475,700 L475,952 L300,952 C310,900 325,860 340,830 C350,790 360,740 372,700Z" fill="url(#guide-photo)"/>

  <!-- topics pill -->
  <rect class="fill-blue" x="-20" y="688" width="319" height="36" rx="18"/>
  <rect class="fill-ink" x="-20" y="691" width="313" height="30" rx="15"/>
  <text class="pill-text" x="33" y="712">Things covered in this 4 hr tour are</text>

  <!-- topics list -->
  <g class="topic-list">
    <g transform="translate(43,753)">
      <circle r="10" class="fill-blue"/><circle r="7" fill="none" stroke="#fff" stroke-width="1.5"/>
      <path d="M0,-4 C2,-1 3,1 3,2 A3,3 0 0 1 -3,2 C-3,1 -2,-1 0,-4Z" class="fill-white"/>
    </g>
    <text class="list-text" x="62" y="758">Finding water</text>
    <g transform="translate(43,782)">
      <circle r="10" class="fill-blue"/><circle r="7" fill="none" stroke="#fff" stroke-width="1.5"/>
      <path d="M-4,1 H4 A4,4 0 0 1 -4,1Z" class="fill-white"/>
    </g>
    <text class="list-text" x="62" y="787">finding food</text>
    <g transform="translate(175,757)">
      <circle r="10" class="fill-blue"/><circle r="7" fill="none" stroke="#fff" stroke-width="1.5"/>
      <path d="M0,-5 C3,-1 4,1 3,3 A3,3 0 0 1 -3,3 C-4,1 -2,-1 0,-5Z" class="fill-white"/>
    </g>
    <text class="list-text"><tspan x="198" y="758">Finding/making</tspan><tspan x="198" y="774">shelter and fire.</tspan></text>
    <g transform="translate(175,793)">
      <circle r="10" class="fill-blue"/><circle r="7" fill="none" stroke="#fff" stroke-width="1.5"/>
      <path d="M-4,0 L0,-4 L4,0 V4 H-4Z" class="fill-white"/>
    </g>
    <text class="list-text"><tspan x="198" y="797">Finding your way</tspan><tspan x="198" y="813">home.</tspan></text>
  </g>

  <!-- call band -->
  <polygon points="0,880 300,952 0,952" fill="url(#front-blue)"/>
  <polygon class="fill-ink" points="0,822 270,908 262,938 0,862"/>
  <text class="call call--light" transform="translate(22,850) rotate(17.5)">CALL 08 5550 0142</text>
</svg>
</div>

<!-- BACK SIDE -->
<div class="flyer flyer--back">
<svg viewBox="0 0 475 952" xmlns="http://www.w3.org/2000/svg">
  <defs>
    <linearGradient id="back-paper" x1="0" y1="0" x2="0" y2="1">
      <stop offset="0" stop-color="#ffffff"/>
      <stop offset=".45" stop-color="#e6e6e6"/>
      <stop offset=".75" stop-color="#c9c9c9"/>
      <stop offset="1" stop-color="#dedede"/>
    </linearGradient>
    <linearGradient id="fruit-photo" x1="0" y1="0" x2="1" y2="1">
      <stop offset="0" stop-color="#c9a590"/>
      <stop offset=".5" stop-color="#6f9a3e"/>
      <stop offset="1" stop-color="#b8a08a"/>
    </linearGradient>
    <linearGradient id="branch-photo" x1="0" y1="0" x2="1" y2="1">
      <stop offset="0" stop-color="#9cc7e6"/>
      <stop offset=".55" stop-color="#7a6450"/>
      <stop offset="1" stop-color="#e79a2a"/>
    </linearGradient>
    <linearGradient id="palm-photo" x1="0" y1="0" x2="0" y2="1">
      <stop offset="0" stop-color="#bcd9ea"/>
      <stop offset=".5" stop-color="#4f8a34"/>
      <stop offset="1" stop-color="#c9a878"/>
    </linearGradient>
    <linearGradient id="catch-photo" x1="0" y1="0" x2="1" y2="1">
      <stop offset="0" stop-color="#b89a80"/>
      <stop offset="1" stop-color="#4a4a42"/>
    </linearGradient>
    <linearGradient id="back-bottom" x1="0" y1="0" x2="1" y2="0">
      <stop offset="0" stop-color="#0b0b0c"/>
      <stop offset="1" stop-color="#2b2c2f"/>
    </linearGradient>
    <filter id="back-shadow" x="-20%" y="-20%" width="140%" height="140%">
      <feDropShadow dx="0" dy="6" stdDeviation="6" flood-opacity=".3"/>
    </filter>
  </defs>

  <rect width="475" height="952" fill="url(#back-paper)"/>

  <!-- corner accents -->
  <polygon class="fill-blue" points="0,0 12,0 150,138 0,288"/>
  <polygon class="fill-ink" points="30,0 62,0 112,50 96,66"/>
  <polygon class="fill-ink" points="0,300 132,168 146,182 0,325"/>
  <polygon class="fill-blue" points="475,178 475,392 368,290"/>
  <polygon class="fill-ink" points="350,328 475,428 475,452 336,342"/>
  <polygon class="fill-ink" points="200,162 212,174 200,186 188,174"/>

  <!-- photo diamonds -->
  <g filter="url(#back-shadow)">
    <polygon class="fill-white" points="127,16 236,125 127,234 18,125"/>
    <polygon class="fill-white" points="368,16 476,124 368,232 260,124"/>
    <polygon class="fill-white" points="250,140 392,282 250,424 108,282"/>
  </g>
  <polygon role="img" aria-label="Photo of native bush fruit held in hand" points="127,22 230,125 127,228 24,125" fill="url(#fruit-photo)"/>
  <polygon class="stroke-blue" points="127,22 230,125 127,228 24,125" style="stroke-width:4"/>
  <polygon role="img" aria-label="Photo of a branch with ripe orange bush fruit" points="368,22 470,124 368,226 266,124" fill="url(#branch-photo)"/>
  <polygon class="stroke-blue" points="368,22 470,124 368,226 266,124" style="stroke-width:4"/>
  <polygon role="img" aria-label="Photo of pandanus palm leaves" points="250,147 385,282 250,417 115,282" fill="url(#palm-photo)"/>
  <polygon class="stroke-blue" points="250,147 385,282 250,417 115,282" style="stroke-width:4"/>

  <!-- copy -->
  <text class="body-copy body-copy--small">
    <tspan x="30" y="444" textLength="425" lengthAdjust="spacing">Clients will then be dropped back to their accomodation with some</tspan>
    <tspan x="30" y="460">fun and vital knowledge of surviving in the Australian outback.</tspan>
    <tspan x="30" y="493" textLength="425" lengthAdjust="spacing">At the end of the tour the group will be able to take home a basic</tspan>
    <tspan x="30" y="510" textLength="425" lengthAdjust="spacing">survival kit which they will be able to use through the skills they</tspan>
    <tspan x="30" y="526">just gained on the tour.</tspan>
  </text>
  <rect x="55" y="548" width="368" height="2" fill="#c4c4c4"/>

  <!-- feature row 1 -->
  <rect class="fill-blue" x="80" y="600" width="310" height="6"/>
  <rect class="fill-blue" x="80" y="717" width="310" height="6"/>
  <g class="feature" transform="translate(80,603)">
    <polygon points="0,-32 32,0 0,32 -32,0" class="fill-blue"/>
    <polygon points="0,-26 26,0 0,26 -26,0" class="fill-white"/>
    <circle cx="0" cy="0" r="10" class="icon-line"/><path d="M0,-6 V0 L5,3" class="icon-line"/>
  </g>
  <g class="feature" transform="translate(237,603)">
    <polygon points="0,-32 32,0 0,32 -32,0" class="fill-blue"/>
    <polygon points="0,-26 26,0 0,26 -26,0" class="fill-white"/>
    <circle cx="-5" cy="-9" r="3" class="fill-ink"/><rect x="-8" y="-5" width="6" height="14" rx="2" class="fill-ink"/>
    <circle cx="6" cy="-9" r="3" class="fill-ink"/><path d="M2,-5 H10 L12,5 H0Z" class="fill-ink"/>
  </g>
  <g class="feature" transform="translate(390,603)">
    <polygon points="0,-32 32,0 0,32 -32,0" class="fill-blue"/>
    <polygon points="0,-26 26,0 0,26 -26,0" class="fill-white"/>
    <rect x="-11" y="-7" width="22" height="17" rx="2" class="fill-ink"/>
    <path d="M-4,-7 V-11 H4 V-7" class="icon-line"/>
    <path d="M0,-3 V6 M-4.5,1.5 H4.5" stroke="#fff" stroke-width="2.4"/>
  </g>
  <text class="feature-text" x="82" y="658" text-anchor="middle">4hr/half day tour</text>
  <text class="feature-text" x="237" y="661" text-anchor="middle">Fun for the family</text>
  <text class="feature-text" text-anchor="middle"><tspan x="384" y="653">Free survival</tspan><tspan x="384" y="670">kit included.</tspan></text>

  <!-- feature row 2 -->
  <g class="feature" transform="translate(80,720)">
    <polygon points="0,-32 32,0 0,32 -32,0" class="fill-blue"/>
    <polygon points="0,-26 26,0 0,26 -26,0" class="fill-white"/>
    <path d="M-9,-4 H9 A9,9 0 0 1 -9,-4Z" class="fill-ink"/><path d="M-6,8 H6" class="icon-line"/>
  </g>
  <g class="feature" transform="translate(237,720)">
    <polygon points="0,-32 32,0 0,32 -32,0" class="fill-blue"/>
    <polygon points="0,-26 26,0 0,26 -26,0" class="fill-white"/>
    <path d="M0,-11 L-10,9 H10Z M-5,-13 L5,5 M5,-13 L-5,5" class="icon-line"/>
  </g>
  <g class="feature" transform="translate(390,720)">
    <polygon points="0,-32 32,0 0,32 -32,0" class="fill-blue"/>
    <polygon points="0,-26 26,0 0,26 -26,0" class="fill-white"/>
    <circle cx="3" cy="-10" r="3" class="fill-ink"/>
    <path d="M1,-6 L-2,3 L-8,10 M-2,3 L5,10 M-8,-3 L1,-6 L8,-2" class="icon-line"/>
  </g>
  <text class="feature-text" x="94" y="768" text-anchor="middle">Eat what you catch</text>
  <text class="feature-text" text-anchor="middle"><tspan x="240" y="770">Learn essential</tspan><tspan x="240" y="787">survival skills</tspan></text>
  <text class="feature-text" text-anchor="middle"><tspan x="384" y="767">Provided buy an</tspan><tspan x="384" y="784">experienced and</tspan><tspan x="384" y="801">passionate bushman.</tspan></text>

  <!-- bottom band -->
  <path role="img" aria-label="Photo of the bushman holding a freshly caught mud crab" d="M0,835 L60,790 L130,800 L175,870 L175,952 L0,952Z" fill="url(#catch-photo)"/>
  <polygon points="155,952 475,846 475,952" fill="url(#back-bottom)"/>
  <polygon class="fill-blue" points="51,952 475,812 475,846 155,952"/>
  <text class="call call--light" transform="translate(215,922) rotate(-18.3)">CALL 08 5550 0142</text>
  <text class="web" x="345" y="942" text-anchor="middle">www.ridgelinewildcraft.com</text>
</svg>
</div>

</body>
</html>
```